Using Existing Logo to Create Stationary, Powerpoint and Word Background Identity

I am seeking an identity design which can be used in corporate literature and documents which extends the use of our new identity within the company logo. I need to specifically have designed background identity for a stationary set which includes a) A4 Front/Title Page (Portrait and Landscape for Proposals (Word) and Powerpoints (PPT)) b) A4 Content Pages (Same as above) c) A4 Letter Template for Letters (Word) d) Business Cards e) A5 With Compliments Slips. It is critical that the road is used in the identity sets and that content pages have clear text space in all instances.

Please read messages, as I am only seeking artwork and example placement of text in a format I can edit using photoshop. Therefore a business card would be layed out per normal with:
Name:
Company:
Mobile:
Phone:
Email:
Fax:
Address:
Web:
etc.

and stationary would have same except name removed. I have increased the budget to $260AU which has not been shown yet??
Updates

I am hoping someone can come up with a unique branding and identity using the road which can translate across business cards, proposals, presentations etc. I have seen previous work by other quality designers in this area that takes a standard logo image and creates an identity across communications documents and stationary. This is what I seek to achieve. If the identity is created for cards and proposals etc then blanks of each template can be provided as PDF, JPG and editable format (photoshop preferred) which we will alter to allow publishing to take place. Thanks

Can we fit the following on the backside of the card.

- Automating Chain of Responsibility
- Simplifying BKTOF & Lorimex
- Providing Eco-Driving & DPWO Reporting
- Protecting Transport Company Executives

Please change the back of card to these:
- Paperless BKTOF & Lorimex
- Electronic Work Diaries, Safe Driving Plans

All,

A great effort and very hard to determine who gets the gig. Each designer brings a unique flavour to this task. I have eliminated all designs that I do not consider meet the brief (per my opinion).

I will work through with those designers to elaborate the design (where needed) to finalise a design concept, which can then be closed and paid.

Please be patient, and I will be in touch shortly.

Marisol

Thanking all designers for their terrific input. We will announce shortly the design concept we are moving forward with. It has taken much deliberation and was difficult to agree upon.

Target Market(s)

Corporate Transport Customers, Government Departments

Industry/Entity Type

Business

Requirements
Must have
• Must use the existing logo imagery to consolidate into a professional identity set.
Nice to have
• Use of Road in design formats

```html
<!DOCTYPE html>
<html lang="en">
<head>
<meta charset="utf-8">
<title>Small Envelopes – RouteLedger Stationery</title>
<link href="https://fonts.googleapis.com/css2?family=Inter:wght@400;700;800&display=swap" rel="stylesheet">
<style>
  :root {
    --page-bg: #ffffff;
    --paper: #ffffff;
    --ink: #111111;
    --flap: #0d0d0d;
    --shadow: rgba(0, 0, 0, 0.28);
  }
  * { box-sizing: border-box; margin: 0; padding: 0; }
  html, body {
    width: 1200px;
    height: 848px;
    overflow: hidden;
    background: var(--page-bg);
  }
  .canvas {
    position: relative;
    width: 1200px;
    height: 848px;
    font-family: "Inter", Arial, sans-serif;
    color: var(--ink);
  }
  .section-label {
    position: absolute;
    left: 86px;
    top: 79px;
    font-size: 11px;
    font-weight: 700;
    letter-spacing: -0.1px;
  }

  .envelope {
    position: absolute;
    background: var(--paper);
    box-shadow: 2px 3px 5px var(--shadow);
  }
  .envelope--back {
    left: 85px;
    top: 103px;
    width: 527px;
    height: 266px;
  }
  .envelope--back .flap {
    position: absolute;
    left: 0;
    top: 0;
    width: 527px;
    height: 82px;
  }

  .envelope-open {
    position: absolute;
    left: 576px;
    top: 421px;
    width: 529px;
    height: 350px;
  }
  .envelope-open .flap {
    position: absolute;
    left: 0;
    top: 0;
    width: 529px;
    height: 84px;
  }
  .envelope-open .body {
    position: absolute;
    left: 0;
    top: 83px;
    width: 529px;
    height: 267px;
    background: var(--paper);
    box-shadow: 2px 3px 5px var(--shadow);
    overflow: hidden;
  }
  .road-artwork {
    position: absolute;
    left: 0;
    bottom: 0;
    width: 240px;
    height: 124px;
    background: linear-gradient(160deg, rgba(17,17,17,0) 30%, rgba(17,17,17,0.55) 62%, #111111 100%);
    clip-path: polygon(0 0, 14% 8%, 30% 40%, 60% 78%, 100% 100%, 0 100%);
  }

  .brand {
    position: absolute;
    text-align: right;
    line-height: 1;
  }
  .brand__name {
    display: block;
    font-weight: 800;
    font-size: 21px;
    letter-spacing: -0.8px;
  }
  .brand__tagline {
    display: block;
    font-weight: 700;
    font-size: 5.5px;
    margin-top: 2px;
    letter-spacing: 0.1px;
  }
  .envelope--back .brand {
    right: 28px;
    top: 215px;
  }
  .envelope--back .brand__mark {
    position: absolute;
    left: -22px;
    top: 4px;
    width: 14px;
    height: 14px;
    background: var(--ink);
    border-radius: 50%;
  }
  .envelope-open .brand {
    left: 344px;
    top: 193px;
    text-align: left;
  }
  .envelope-open .brand__tagline { text-align: right; }
  .return-address {
    position: absolute;
    left: 344px;
    top: 229px;
    font-size: 5.5px;
    line-height: 1.4;
    font-weight: 400;
    font-style: normal;
  }
</style>
</head>
<body>
<main class="canvas">
  <p class="section-label">Small Envelopes</p>

  <section class="envelope envelope--back" aria-label="DL envelope, flap view">
    <svg class="flap" viewBox="0 0 527 82" aria-hidden="true">
      <path d="M0 0 H527 V8 L486 70 Q478 82 463 82 H64 Q49 82 41 70 L0 8 Z" fill="var(--flap)"/>
    </svg>
    <div class="brand">
      <span class="brand__mark"></span>
      <span class="brand__name">RouteLedger</span>
      <span class="brand__tagline">Records in Order</span>
    </div>
  </section>

  <section class="envelope-open" aria-label="DL envelope, front with return address">
    <svg class="flap" viewBox="0 0 529 84" aria-hidden="true">
      <path d="M0 84 L14 14 Q17 0 32 0 H497 Q512 0 515 14 L529 84 Z" fill="var(--flap)"/>
    </svg>
    <div class="body">
      <div class="road-artwork" role="img" aria-label="Sweeping black road graphic rising from the lower left corner"></div>
      <div class="brand">
        <span class="brand__name">RouteLedger</span>
        <span class="brand__tagline">Records in Order</span>
      </div>
      <address class="return-address">
        Ashford - Head Office<br>
        Unit 4, 210 Harlow Street, Glenmere Victoria, 3170
      </address>
    </div>
  </section>
</main>
</body>
</html>
```